Visitenkarten-Design für virtuelle Jobmesse & Jobbörse für Soldaten
Zielgruppe
Die KLO GmbH ist ein Unternehmen das zwei Hauptprodukte betreibt! Zum einen Jobbörse für Soldaten unter www.wachwechselpunkt.de und zum anderen eine virtuelle Jobmesse für Soldaten unter www.marvento.de , die wir zweimal im Jahr veranstalten.
Aufgabenstellung
Wir haben ja die beiden Produkte Wachwechselpunkt.de und die Marvento, für die bereits jeweils ein separtes Logo besteht! Diese finden Sie im Anhang! Beide werden doch jedoch von einem Unternehmen, der KLO GmbH betrieben! Aktuell nutzen wir eine Visitenkarte mit dem Logo von KLO und eine mit dem Logo der MARVENTO. Gerade im Hinblick darauf, dass wir zukünftig auch weiter Plattformen in unser Portfolio aufnehmen, möchte ich hier unsere V-Karten flexibler gestalten!
Ziel soll es also sein, eine Visitenkarte zu gestalten, auf dem klar wird, dass der Mitarbeiter von der KLO GmbH kommt, die KLO GmbH aber unterschiedliche Produkte betreibt.
Im Anhang finden Sie:
1. Das Logo von KLO
2. Das Logo von Marvento
3. Die aktuelle V-Karte von KLO
4. Die aktuelle V-Karte von MARVENTO
Vielleicht ein kleiner Anreiz: Aktuell nutzen wir auch zwei getrennte Geschäftspapiere. Das von www.wachwechselpunkt.de lade ich einmal hoch! Der Designer, der auch die Visitenkarte erstellt, erhällt im Anschluss den 1:1 Auftrag in Höhe von 200 Euro für die Erstellung des Geschäftspapiers! Wenn Sie jetzt schon einen Vorschlag für das Geschäftspapier einreichen, erhöht das natürlich Ihre Chancen, wobei ich verspreche, dass wir im Falle eine Annahme das 1:1 im Anschluß dennoch starten werden!

```html
<!DOCTYPE html>
<html lang="de">
<head>
<meta charset="utf-8">
<title>Visitenkarte KLO GmbH</title>
<link href="https://fonts.googleapis.com/css2?family=Arimo:wght@400;700&display=swap" rel="stylesheet">
<style>
  :root {
    --navy-top: #224b7e;
    --navy-bottom: #1a365c;
    --brand-blue: #234a80;
    --text-grey: #8a8a8a;
    --frame: #555555;
    --paper: #ffffff;
    --marvento-green: #3b5a2b;
  }
  * { margin: 0; padding: 0; box-sizing: border-box; }
  html, body {
    width: 848px; height: 1200px; overflow: hidden;
    background: var(--paper);
    font-family: "Arimo", Arial, sans-serif;
  }
  .sheet { position: relative; width: 848px; height: 1200px; }
  .card {
    position: absolute; top: 198px;
    width: 342px; height: 221px;
    border: 1px solid var(--frame);
    background: var(--paper);
    overflow: hidden;
  }
  .card--front { left: 75px; }
  .card--back { left: 436px; }

  .front__arc { position: absolute; left: 0; top: 0; }
  .person { position: absolute; left: 19px; top: 87px; color: #fff; }
  .person__name { font-size: 16.4px; font-weight: 700; line-height: 19px; }
  .person__role { font-size: 11.6px; line-height: 14px; }

  .company { position: absolute; left: 176px; top: 84px; right: 8px; color: var(--text-grey); }
  .company__name { font-size: 20.5px; font-weight: 700; color: var(--brand-blue); line-height: 24px; margin-bottom: 4px; }
  .company__group { font-size: 11.6px; line-height: 14px; margin-bottom: 4.5px; white-space: nowrap; }

  .brands-tab {
    position: absolute; left: 103px; top: 0;
    width: 132px; height: 27px;
    background: linear-gradient(var(--navy-top), var(--navy-bottom));
    border-radius: 0 0 8px 8px;
    color: #fff; font-size: 13.7px; text-align: center; line-height: 26px;
  }
  .brand {
    position: absolute; display: flex; align-items: center; justify-content: center;
    gap: 5px; font-size: 12px; font-weight: 700; white-space: nowrap;
  }
  .brand--wachwechsel { left: 36px; top: 88px; width: 124px; height: 28px; color: var(--brand-blue); }
  .brand--marvento { left: 180px; top: 70px; width: 126px; height: 66px; color: var(--marvento-green); font-size: 15px; }
  .brand__mark--square { flex-shrink: 0; width: 8px; height: 8px; background: var(--brand-blue); }
  .brand__mark--circle { flex-shrink: 0; width: 10px; height: 10px; border-radius: 50%; background: var(--marvento-green); }
</style>
</head>
<body>
<main class="sheet">
  <section class="card card--front">
    <svg class="front__arc" width="342" height="221" viewBox="0 0 342 221" aria-hidden="true">
      <defs>
        <linearGradient id="navyFade" x1="0" y1="0" x2="0" y2="1">
          <stop offset="0" stop-color="#224b7e"/>
          <stop offset="1" stop-color="#1a365c"/>
        </linearGradient>
      </defs>
      <circle cx="-1.3" cy="109" r="161.3" fill="url(#navyFade)"/>
    </svg>
    <div class="person">
      <p class="person__name">Lukas Beispiel</p>
      <p class="person__role">Geschäftsführer</p>
    </div>
    <div class="company">
      <p class="company__name">KLO GmbH</p>
      <p class="company__group">Lindenweg 7<br>86650 Ahrenfeld</p>
      <p class="company__group">Telefon 08451 - 318 62 07<br>Mobil 0157 - 482 19 306</p>
      <p class="company__group">lb@wachwechselpunkt.de<br>www.wachwechselpunkt.de</p>
    </div>
  </section>

  <section class="card card--back">
    <div class="brands-tab">Unsere Marken</div>
    <div class="brand brand--wachwechsel"><span class="brand__mark--square"></span>Wachwechselpunkt</div>
    <div class="brand brand--marvento"><span class="brand__mark--circle"></span>MARVENTO</div>
  </section>
</main>
</body>
</html>
```